Long Established Local Fencing (not swords) Business needs fresh Business Cards

We need fresh double sided business cards for our Fencing Construction business, we are looking for something with our new logo design added, and maybe a photo background ?
We recently had cards made from Cardlyne and we were horrified with what we got back, the quality was terrible, so am looking for high quality format for good printing company to make.
We install Steelmora, Timber paling, Aluminium Slat Screening, Picket (timber and aluminium) and most other fencing installations.
Our website is brankelrails.com.au should you like to learn a bit more.
We do have logo in other formats if required.
We have been in business for over 35 years and we have used this as a "motto" it is on our signage

Industry/Entity Type

Construction

Contact Information for Business Card

Open to ideas, we need 3 x different cards, one generic with no name and 2 x others each with 1 of our bosses name on each, I will put into upload files.

Colors
ec1f27
000000
606060
f5f5f5

Requirements
Must have
• Company Name and Logo
• Address
• Contact details, phone, website, email etc
• Small space to write notes when leaving card at residence
Nice to have
• Our motto "Building fences along the coast for 35 years"

```html
<!DOCTYPE html>
<html lang="en">
<head>
<meta charset="utf-8">
<title>Brankel Fencing – Business Cards</title>
<link rel="stylesheet" href="https://fonts.googleapis.com/css2?family=Michroma&family=Roboto:wght@700&display=swap">
<style>
  :root {
    --red: #ec1f27;
    --red-deep: #c8161d;
    --black: #000000;
    --grey: #606060;
    --offwhite: #f5f5f5;
    --white: #ffffff;
    --stage: #3b3c3f;
    --rule: #a9a9a9;
  }
  * { margin: 0; padding: 0; box-sizing: border-box; }
  html, body { width: 1200px; height: 1000px; overflow: hidden; }
  body { background: var(--stage); position: relative; font-family: "Michroma", sans-serif; }

  .card { position: absolute; width: 557px; height: 319px; background: var(--white); overflow: hidden; }
  .card--mark { left: 28px; top: 93px; }
  .card--dale { left: 616px; top: 93px; }
  .card--generic { left: 28px; top: 534px; }
  .card--front { left: 616px; top: 534px; background: var(--offwhite); }

  .card__photo { position: absolute; left: 0; top: 0; width: 100%; height: 207px;
    background: linear-gradient(100deg, var(--red-deep) 0%, var(--red) 45%, #e0242b 100%); }
  .card__band { position: absolute; left: 0; top: 207px; width: 100%; height: 16px; background: var(--grey); }
  .card__note-line { position: absolute; left: 30px; right: 30px; height: 1px; background: var(--rule); }
  .card__note-line--1 { top: 255px; }
  .card__note-line--2 { top: 289px; }

  .card__details { position: absolute; color: var(--white); -webkit-text-stroke: 0.35px var(--white); }
  .card--mark .card__details, .card--dale .card__details { left: 97px; top: 24px; }
  .card--generic .card__details { left: 62px; top: 50px; }

  .person-name { font-size: 25px; line-height: 30px; letter-spacing: 0.5px; -webkit-text-stroke: 0.9px var(--white); }
  .licence { font-size: 10px; line-height: 12px; margin-bottom: 16px; }
  .contact-row { display: flex; font-size: 13px; line-height: 24px; letter-spacing: 0.4px; }
  .contact-row__label { width: 93px; }
  .contact-row--gap { margin-top: 13px; }
  .card--generic .contact-row { font-size: 15px; line-height: 28px; }
  .card--generic .contact-row__label { width: 108px; }
  .card--generic .contact-row--gap { margin-top: 16px; }

  .front__edge { position: absolute; top: 0; height: 100%; }
  .front__edge--red-left { left: 0; width: 49px; background: var(--red); }
  .front__edge--grey-left { left: 49px; width: 15px; background: var(--grey); }
  .front__edge--grey-right { right: 49px; width: 15px; background: var(--grey); }
  .front__edge--red-right { right: 0; width: 49px; background: var(--red); }
  .front__brand { position: absolute; left: 64px; right: 64px; top: 34px; text-align: center; }
  .front__brand-mark { width: 70px; height: 70px; margin: 0 auto 30px; background: var(--red); }
  .front__brand-name { font-size: 36px; line-height: 46px; color: var(--black); letter-spacing: 1px; font-weight: 400; }
  .front__motto { position: absolute; left: 64px; right: 64px; top: 266px; text-align: center; font-size: 13px; color: var(--black); -webkit-text-stroke: 0.3px var(--black); }
  .front__address { position: absolute; left: 64px; right: 64px; top: 292px; text-align: center; font-size: 11.5px; color: var(--grey); }

  .caption { position: absolute; width: 557px; text-align: center; color: var(--white);
    font-family: "Roboto", sans-serif; font-weight: 700; font-size: 30px; }
  .caption--mark { left: 28px; top: 426px; }
  .caption--dale { left: 616px; top: 426px; }
  .caption--generic { left: 28px; top: 873px; }
  .caption--front { left: 616px; top: 873px; }
</style>
</head>
<body>

<section class="card card--mark">
  <div class="card__photo" role="img" aria-label="Red-toned photo of a metal pool fence and garden"></div>
  <div class="card__details">
    <h2 class="person-name">ROWAN PIKE</h2>
    <p class="licence">License No. 40211C</p>
    <p class="contact-row"><span class="contact-row__label">Phone:</span><span>(02) 4390 2215</span></p>
    <p class="contact-row"><span class="contact-row__label">Mobile:</span><span>0432 555 018</span></p>
    <p class="contact-row contact-row--gap"><span class="contact-row__label">Email:</span><span>office@brankelrails.com.au</span></p>
    <p class="contact-row"><span class="contact-row__label">Website:</span><span>www.brankelrails.com.au</span></p>
  </div>
  <div class="card__band"></div>
  <div class="card__note-line card__note-line--1"></div>
  <div class="card__note-line card__note-line--2"></div>
</section>
<p class="caption caption--mark">ROWAN PIKE</p>

<section class="card card--dale">
  <div class="card__photo" role="img" aria-label="Red-toned photo of a metal pool fence and garden"></div>
  <div class="card__details">
    <h2 class="person-name">DALE MERROW</h2>
    <p class="licence">License No. 40211C</p>
    <p class="contact-row"><span class="contact-row__label">Phone:</span><span>(02) 4390 2215</span></p>
    <p class="contact-row"><span class="contact-row__label">Mobile:</span><span>0413 555 402</span></p>
    <p class="contact-row contact-row--gap"><span class="contact-row__label">Email:</span><span>office@brankelrails.com.au</span></p>
    <p class="contact-row"><span class="contact-row__label">Website:</span><span>www.brankelrails.com.au</span></p>
  </div>
  <div class="card__band"></div>
  <div class="card__note-line card__note-line--1"></div>
  <div class="card__note-line card__note-line--2"></div>
</section>
<p class="caption caption--dale">DALE MERROW</p>

<section class="card card--generic">
  <div class="card__photo" role="img" aria-label="Red-toned photo of a metal pool fence and garden"></div>
  <div class="card__details">
    <p class="contact-row"><span class="contact-row__label">Phone:</span><span>4390 2215</span></p>
    <p class="contact-row"><span class="contact-row__label">Mobile:</span><span>0413 555 402</span></p>
    <p class="contact-row contact-row--gap"><span class="contact-row__label">Email:</span><span>office@brankelrails.com.au</span></p>
    <p class="contact-row"><span class="contact-row__label">Website:</span><span>www.brankelrails.com.au</span></p>
  </div>
  <div class="card__band"></div>
  <div class="card__note-line card__note-line--1"></div>
  <div class="card__note-line card__note-line--2"></div>
</section>
<p class="caption caption--generic">GENERIC</p>

<section class="card card--front">
  <div class="front__edge front__edge--red-left"></div>
  <div class="front__edge front__edge--grey-left"></div>
  <div class="front__edge front__edge--grey-right"></div>
  <div class="front__edge front__edge--red-right"></div>
  <div class="front__brand">
    <div class="front__brand-mark"></div>
    <h1 class="front__brand-name">BRANKEL<br>FENCING</h1>
  </div>
  <p class="front__motto">Building fences along the coast for 35 years</p>
  <p class="front__address">27 Tern Avenue, Brankel Bay, NSW 2419</p>
</section>
<p class="caption caption--front">FRONT PART</p>

</body>
</html>
```